project - Kestra Nook

Dear designers, I'm Looking for an appealing new business card design to represent us for our new e-cigarette store: The KestrA Nook. Knowledgeable and friendly staff we aim for superior customer service with a positive atmosphere. Classic feel with modern touch is what we are aiming for . Lime green font and grey back round is the original color scheme but we are flexible and open to suggestions. I added some doodles to show you where my mind is at. address: 4308 87 Ave NW Edmonton, AB (inside the hollin trade hall)web: thekestranook.com email: info@thekestranook.com phone : 587.555.0148 Thanks and am looking forward to seeing your creative , fresh and innovative designs.
Good luck everybody!
Jonas
lime green and charcoal grey please. thanks
Business
The KestrA Nook

```html
<!DOCTYPE html>
<html lang="en">
<head>
<meta charset="utf-8">
<title>The KestrA Nook — Business Card</title>
<link href="https://fonts.googleapis.com/css2?family=Arimo:wght@400;700&family=Gochi+Hand&display=swap" rel="stylesheet">
<style>
  :root {
    --backdrop: #ececec;
    --card: #c6c6c6;
    --lime: #45ad4c;
    --smoke-strong: rgba(88, 180, 96, 0.55);
    --smoke-soft: rgba(88, 180, 96, 0);
  }
  * { margin: 0; padding: 0; box-sizing: border-box; }
  html, body {
    width: 1200px; height: 720px; overflow: hidden;
    background: var(--backdrop);
  }
  .canvas {
    position: relative; width: 1200px; height: 720px;
    display: flex; justify-content: center; align-items: center; gap: 40px;
  }
  .card {
    position: relative; width: 440px; height: 252px;
    background: var(--card); color: var(--lime);
    font-family: "Arimo", Arial, sans-serif;
  }
  .smoke {
    position: absolute;
    background: radial-gradient(ellipse at center, var(--smoke-strong) 0%, var(--smoke-soft) 70%);
  }
  .brand-name {
    position: absolute; left: 0; right: 0; text-align: center;
    font-family: "Arimo", Arial, sans-serif; font-weight: 700;
    color: var(--lime); white-space: nowrap;
  }
  /* front */
  .card-front .smoke { left: 215px; top: 70px; width: 170px; height: 120px; }
  .card-front .brand-name { top: 108px; font-size: 34px; }
  .card-front .web {
    position: absolute; left: 0; right: 0; top: 192px; text-align: center;
    font-size: 12px; font-weight: 700; letter-spacing: 2.6px;
  }
  /* back */
  .card-back .smoke { left: 200px; top: 8px; width: 150px; height: 70px; }
  .card-back .brand-name { top: 36px; font-size: 20px; }
  .tagline {
    position: absolute; left: 0; right: 0; top: 80px; text-align: center;
    font-family: "Gochi Hand", cursive; font-size: 28px; letter-spacing: 1px;
  }
  .contact {
    position: absolute; left: 0; right: 0; top: 128px; text-align: center;
    font-size: 12.5px; font-weight: 700; line-height: 23px;
  }
  .contact .label { font-style: italic; font-family: Georgia, serif; margin-right: 4px; }
  .address { margin-top: 6px; line-height: 20px; }
</style>
</head>
<body>
<main class="canvas">
  <section class="card card-front">
    <div class="smoke" role="img" aria-label="Soft green smoke wisp drifting behind the store name"></div>
    <h1 class="brand-name">The KestrA Nook</h1>
    <p class="web">thekestranook.com</p>
  </section>

  <section class="card card-back">
    <div class="smoke" role="img" aria-label="Soft green smoke wisp drifting behind the store name"></div>
    <h2 class="brand-name">The KestrA Nook</h2>
    <p class="tagline">e-cigarette store</p>
    <div class="contact">
      <p><span class="label">Phone :</span>587.555.0148</p>
      <p><span class="label">Email:</span>info@thekestranook.com</p>
      <p class="address">4308 87 Ave NW Edmonton, AB<br>(inside the hollin trade hall)</p>
    </div>
  </section>
</main>
</body>
</html>
```